Business Card Design - Cryotherapy

We need a custom created business card for our company FrostLume Spa. We provide whole body cryotherapy and localized cryotherapy to our clients. Please be creative.
Please see our website for idea's on design.
www.frostlumespa.com
Industry/Entity Type
Business
Contact Information for Business Card
Name, Position, Phone Number, Address, Website, Email
Look and feel
Each slider illustrates characteristics of the customer's brand and the style your logo design should communicate.

```html
<!DOCTYPE html>
<html lang="en">
<head>
<meta charset="utf-8">
<title>FrostLume Spa – Business Card</title>
<link rel="stylesheet" href="https://fonts.googleapis.com/css2?family=Source+Sans+3:wght@300;400&family=Crimson+Text:wght@400&display=swap">
<style>
  :root {
    --page-bg: #e9ecee;
    --card-white: #fbfbfb;
    --teal: #1bb3bf;
    --teal-deep: #0aa3b0;
    --teal-light: #35d3dc;
    --ink: #4a4a4a;
    --ink-soft: #6b6b6b;
    --white: #ffffff;
  }
  * { margin: 0; padding: 0; box-sizing: border-box; }
  html, body { width: 1200px; height: 1062px; overflow: hidden; }
  body {
    background: var(--page-bg);
    font-family: "Source Sans 3", "Helvetica Neue", Arial, sans-serif;
    position: relative;
  }
  .card {
    position: absolute;
    width: 640px;
    height: 366px;
    border-radius: 2px;
    box-shadow: 0 10px 28px rgba(0,0,0,0.16), 0 2px 5px rgba(0,0,0,0.08);
    overflow: hidden;
  }
  /* Front side */
  .card-front {
    left: 70px; top: 90px;
    background: radial-gradient(ellipse at 55% 40%, #ffffff 0%, var(--card-white) 60%, #eeeeee 100%);
    color: var(--ink);
  }
  .holder { position: absolute; left: 44px; top: 40px; }
  .holder-name {
    font-family: "Crimson Text", Georgia, serif;
    font-size: 28px; color: var(--teal); line-height: 1.1;
  }
  .holder-role {
    font-family: "Crimson Text", Georgia, serif;
    font-size: 18px; color: var(--ink); margin-top: 2px;
  }
  .brand-lockup {
    position: absolute; left: 190px; top: 150px;
    display: flex; align-items: center; gap: 14px;
  }
  .brand-dot { width: 22px; height: 22px; border-radius: 50%; background: var(--teal); }
  .brand-name {
    font-weight: 300; font-size: 50px; letter-spacing: 1px;
    color: var(--teal); line-height: 1;
  }
  .contact-list {
    position: absolute; left: 190px; top: 250px;
    list-style: none; font-size: 17px; font-weight: 300; color: var(--ink-soft);
  }
  .contact-list li { display: flex; align-items: center; gap: 10px; line-height: 1.55; }
  .contact-list svg, .address svg { width: 14px; height: 14px; flex: none; }
  .address {
    position: absolute; right: 40px; top: 260px;
    display: flex; gap: 10px; align-items: flex-start;
    font-size: 17px; font-weight: 300; color: var(--ink-soft); line-height: 1.45;
  }
  .address svg { margin-top: 4px; }

  /* Back side */
  .card-back {
    left: 490px; top: 600px;
    background: radial-gradient(ellipse at 45% 55%, var(--teal-light) 0%, var(--teal) 50%, var(--teal-deep) 100%);
  }
  .back-halo {
    position: absolute; left: 60px; top: 40px; width: 240px; height: 240px;
    border-radius: 50%; background: rgba(255,255,255,0.16);
  }
  .back-brand {
    position: absolute; right: 50px; bottom: 70px;
    font-weight: 300; font-size: 54px; letter-spacing: 1px; color: var(--white);
  }
</style>
</head>
<body>

<section class="card card-front" aria-label="Business card front">
  <div class="holder">
    <p class="holder-name">Dana Whitlow</p>
    <p class="holder-role">Manager</p>
  </div>

  <div class="brand-lockup">
    <span class="brand-dot"></span>
    <span class="brand-name">FrostLume Spa</span>
  </div>

  <ul class="contact-list">
    <li>
      <svg viewBox="0 0 16 16" aria-hidden="true"><path d="M4 1.5l2.2 3-1.4 1.6c.9 1.9 2.3 3.3 4.2 4.2l1.6-1.4 3 2.2-1.3 2.4C7 13.3 2.7 9 1.5 3.2z" fill="var(--teal)"/></svg>
      555 201 4488
    </li>
    <li>
      <svg viewBox="0 0 16 16" aria-hidden="true"><circle cx="8" cy="8" r="6.5" fill="none" stroke="var(--teal)" stroke-width="1.4"/><path d="M1.5 8h13M8 1.5c-3 3.5-3 9.5 0 13M8 1.5c3 3.5 3 9.5 0 13" fill="none" stroke="var(--teal)" stroke-width="1.1"/></svg>
      www.danawhitlow.com
    </li>
    <li>
      <svg viewBox="0 0 16 16" aria-hidden="true"><circle cx="8" cy="8" r="2.6" fill="none" stroke="var(--teal)" stroke-width="1.5"/><path d="M10.6 6v3c0 1.6 2.9 1.6 2.9-1 0-3.2-2.5-5.6-5.5-5.6S2.5 4.8 2.5 8s2.5 5.6 5.5 5.6c1.2 0 2.2-.3 3-.8" fill="none" stroke="var(--teal)" stroke-width="1.5"/></svg>
      dana@frostlumespa.com
    </li>
  </ul>

  <div class="address">
    <svg viewBox="0 0 16 16" aria-hidden="true"><path d="M8 1a4.5 4.5 0 0 0-4.5 4.5C3.5 9 8 15 8 15s4.5-6 4.5-9.5A4.5 4.5 0 0 0 8 1zm0 6.2a1.7 1.7 0 1 1 0-3.4 1.7 1.7 0 0 1 0 3.4z" fill="var(--teal)"/></svg>
    <p>Suite 48 Harbor Lane<br>Coral Bay, FL</p>
  </div>
</section>

<section class="card card-back" aria-label="Business card back">
  <div class="back-halo"></div>
  <p class="back-brand">FrostLume Spa</p>
</section>

</body>
</html>
```